Letterhead and Business Cards

Using our new logo we would like designs for the following,

1.Letterhead

2. 2 x Business Cards

I will need all three in high quality PDF files ready for printing. I will also require the top and bottom of the letterhead as two JPG files.

Target Market(s)

We are a business to business company dealing with middle to upper management both as clients and suppliers.

Industry/Entity Type

Business

Requirements
Must have
• 1. Look professional.
• 2. Utilise our logo colours
• 3. Incorporate our logo on both.
• 4. Letterhead

• Address:
• Kelmont Yard House
• Kelmont Yard Lane
• London
• SE9 4TQ

• Tel:0845 312 4096
• Fax: 0845 312 7041
• Website: www.quillomarket.example
• Email: info@quillomarket.example

• Directors: G.H. Pomfrey and M.R. Pomfrey Company Registration No: 52640918(This should be quite small in the letterhead footer somewhere)

• Business Card One Sided Only

• 1. Gideon H. Pomfrey
• Managing Director

• Address:
• Kelmont Yard House
• Kelmont Yard Lane
• London
• SE9 4TQ

• Tel:0845 312 4096
• Fax: 0845 312 7042
• Mob: 0791 563 2208
• Email: gideon@quillomarket.example

• 2. Miriam R. Pomfrey
• Sales Director

• Address:
• Kelmont Yard House
• Kelmont Yard Lane
• London
• SE9 4TQ

• Tel:0845 312 4096
• Fax: 0845 312 7041
• Mob: 0794 826 1159
• Email: miriam@quillomarket.example

• Please note some of this info may change for final printing.

```html
<!DOCTYPE html>
<html lang="en">
<head>
<meta charset="utf-8">
<title>Quillo Market Stationery</title>
<link rel="stylesheet" href="https://fonts.googleapis.com/css2?family=Arimo:wght@400;700&display=swap">
<style>
  :root {
    --brand-green: #6fd11f;
    --accent-green: #8ccc00;
    --rule-green: #7cc21a;
    --ink: #231f20;
    --ink-soft: #3a3a3a;
    --band-grey: #b3b3b3;
    --frame: #555;
    --paper: #fff;
  }
  * { margin: 0; padding: 0; box-sizing: border-box; }
  html, body { width: 993px; height: 1200px; overflow: hidden; background: var(--paper); }
  body { position: relative; font-family: "Arimo", Arial, sans-serif; color: var(--ink); }

  .letterhead {
    position: absolute; left: 162px; top: 0; width: 818px; height: 1156px;
    border: 1px solid var(--frame); background: var(--paper);
  }
  .brand { position: absolute; display: flex; flex-direction: column; align-items: center; }
  .brand__dot { border-radius: 50%; background: var(--brand-green); }
  .brand__name { color: var(--brand-green); font-weight: 700; white-space: nowrap; }

  .letterhead .brand { left: 38px; top: 40px; width: 153px; }
  .letterhead .brand__dot { width: 66px; height: 66px; margin-bottom: 10px; }
  .letterhead .brand__name { font-size: 21px; }

  .directors { position: absolute; left: 627px; top: 54px; }
  .directors__label { font-size: 11.5px; font-weight: 700; color: var(--ink-soft); }
  .directors__names { font-size: 11.5px; color: var(--ink-soft); margin-top: 4px; }
  .directors__rule { position: absolute; left: 627px; top: 96px; width: 191px; height: 2px; background: var(--rule-green); }
  .registration { position: absolute; left: 627px; top: 109px; font-size: 8.6px; letter-spacing: 0.3px; color: var(--ink-soft); }

  .footer__rule { position: absolute; left: 38px; top: 1088px; width: 741px; height: 1.5px; background: var(--rule-green); }
  .footer__address {
    position: absolute; left: 20px; width: 778px; top: 1099px;
    text-align: center; font-size: 11px; line-height: 18px; white-space: nowrap;
  }

  .card {
    position: absolute; left: 0; width: 332px; height: 216px;
    border: 1px solid var(--frame); background: var(--paper); overflow: hidden;
  }
  .card--md { top: 349px; }
  .card--sd { top: 631px; }
  .card .brand { left: 14px; top: 20px; width: 120px; }
  .card .brand__dot { width: 56px; height: 56px; margin-bottom: 9px; }
  .card .brand__name { font-size: 16px; }
  .card__web { position: absolute; left: 17px; top: 103px; font-size: 9px; letter-spacing: 0.9px; color: var(--ink-soft); }
  .card__person { position: absolute; right: 25px; top: 19px; text-align: right; }
  .card__name { font-size: 13.6px; font-weight: 700; color: var(--ink-soft); }
  .card__title { font-size: 9px; color: var(--ink-soft); margin-top: 3px; }
  .card__tab { position: absolute; right: 0; top: 20px; width: 16px; height: 26px; background: var(--accent-green); }
  .card__band {
    position: absolute; left: 0; right: 0; bottom: 0; height: 86px; background: var(--band-grey);
    font-size: 10.6px; line-height: 14.8px;
  }
  .card__address { position: absolute; left: 14px; top: 12px; }
  .card__contact { position: absolute; right: 16px; top: 11px; text-align: right; white-space: nowrap; }
</style>
</head>
<body>

<section class="letterhead">
  <div class="brand">
    <span class="brand__dot"></span>
    <span class="brand__name">Quillo Market</span>
  </div>
  <div class="directors">
    <p class="directors__label">Directors:</p>
    <p class="directors__names">G.H. Pomfrey &nbsp;I&nbsp; M.R. Pomfrey</p>
  </div>
  <div class="directors__rule"></div>
  <p class="registration">Company Registration No: 52640918</p>

  <div class="footer__rule"></div>
  <p class="footer__address">
    Kelmont Yard House, Kelmont Yard Lane, London, SE9 4TQ &nbsp;I&nbsp; Tel : 0845 312 4096 &nbsp;&nbsp;Fax : 0845 312 7041 &nbsp;&nbsp;Email: info@quillomarket.example<br>
    Website: www.quillomarket.example
  </p>
</section>

<article class="card card--md">
  <div class="brand">
    <span class="brand__dot"></span>
    <span class="brand__name">Quillo Market</span>
  </div>
  <p class="card__web">www.quillomarket.example</p>
  <div class="card__person">
    <p class="card__name">Gideon H. Pomfrey</p>
    <p class="card__title">Managing Director</p>
  </div>
  <div class="card__tab"></div>
  <div class="card__band">
    <p class="card__address">Kelmont Yard House<br>Kelmont Yard Lane<br>London<br>SE9 4TQ</p>
    <p class="card__contact">Tel : 0845 312 4096<br>Fax : 0845 312 7042<br>Mob : 0791 563 2208<br>Email: gideon@quillomarket.example</p>
  </div>
</article>

<article class="card card--sd">
  <div class="brand">
    <span class="brand__dot"></span>
    <span class="brand__name">Quillo Market</span>
  </div>
  <p class="card__web">www.quillomarket.example</p>
  <div class="card__person">
    <p class="card__name">Miriam R. Pomfrey</p>
    <p class="card__title">Sales Director</p>
  </div>
  <div class="card__tab"></div>
  <div class="card__band">
    <p class="card__address">Kelmont Yard House<br>Kelmont Yard Lane<br>London<br>SE9 4TQ</p>
    <p class="card__contact">Tel : 0845 312 4096<br>Fax : 0845 312 7042<br>Mob : 0794 826 1159<br>Email: miriam@quillomarket.example</p>
  </div>
</article>

</body>
</html>
```